Corvath Properties Business Card Design

We would now like to design business cards with the new Corvath Properties logo

Target Market(s)

Professional

Industry/Entity Type

Professional services

Contact Information for Business Card

Employee name, title, phone number, email address, corporate office address and logo.

Font styles to use
Sans Serif

Colors
0054AA
0677BA
7BADD7
CADEEF
E8F1F8

Requirements
Must have
• My logo
Should not have
• any other pictures or images besides my logo

```html
<!DOCTYPE html>
<html lang="en">
<head>
<meta charset="UTF-8">
<title>Corvath Properties – Business Card</title>
<link href="https://fonts.googleapis.com/css2?family=Montserrat:wght@400;600;700&display=swap" rel="stylesheet">
<style>
  :root {
    --navy: #0054AA;
    --blue: #0677BA;
    --sky: #7BADD7;
    --mist: #CADEEF;
    --ice: #E8F1F8;
    --page: #eef0f2;
    --white: #ffffff;
  }
  html, body {
    margin: 0;
    padding: 0;
    width: 898px;
    height: 1200px;
    overflow: hidden;
    background: var(--page);
    font-family: "Montserrat", sans-serif;
  }
  .card {
    position: absolute;
    left: 141px;
    top: 40px;
    width: 615px;
    height: 1120px;
    background: var(--ice);
    border-radius: 22px;
    box-shadow: 0 10px 30px rgba(0, 40, 90, 0.12);
  }
  .card-frame {
    position: absolute;
    left: 36px;
    top: 36px;
    right: 36px;
    bottom: 36px;
    border: 3px solid var(--navy);
  }
  .brand {
    position: absolute;
    left: 72px;
    top: 78px;
    width: 468px;
    height: 330px;
    display: flex;
    align-items: center;
    gap: 24px;
  }
  .brand-mark {
    flex: none;
    width: 110px;
    height: 110px;
    background: var(--navy);
  }
  .brand-name {
    margin: 0;
    color: var(--navy);
    font-weight: 700;
    font-size: 36px;
    line-height: 1.15;
    letter-spacing: 1px;
    text-transform: uppercase;
  }
  .contact-panel {
    position: absolute;
    left: 72px;
    top: 475px;
    width: 468px;
    height: 566px;
    background: linear-gradient(180deg, var(--blue) 0%, #1d7fc3 55%, var(--blue) 100%);
    color: var(--white);
  }
  .person-name {
    position: absolute;
    left: 48px;
    top: 72px;
    margin: 0;
    font-size: 32px;
    font-weight: 700;
    color: var(--mist);
  }
  .person-title {
    position: absolute;
    left: 48px;
    top: 120px;
    margin: 0;
    font-size: 23px;
    font-weight: 400;
    color: var(--ice);
  }
  .contact-list {
    position: absolute;
    left: 48px;
    top: 218px;
    margin: 0;
    padding: 0;
    list-style: none;
    font-size: 23px;
    line-height: 38px;
  }
  .contact-list li {
    display: flex;
    align-items: center;
    gap: 14px;
  }
  .contact-icon {
    width: 18px;
    height: 18px;
    flex: none;
  }
  .address {
    position: absolute;
    left: 48px;
    top: 330px;
    margin: 0;
    font-style: normal;
    font-size: 23px;
    line-height: 36px;
  }
  .website {
    position: absolute;
    left: 48px;
    top: 480px;
    margin: 0;
    font-size: 22px;
    color: var(--ice);
  }
</style>
</head>
<body>
  <article class="card">
    <div class="card-frame"></div>

    <header class="brand">
      <div class="brand-mark"></div>
      <h1 class="brand-name">Corvath<br>Properties</h1>
    </header>

    <section class="contact-panel">
      <h2 class="person-name">Marcus Ellery</h2>
      <p class="person-title">Director</p>

      <ul class="contact-list">
        <li>
          <svg class="contact-icon" viewBox="0 0 24 24" aria-hidden="true">
            <path d="M6.6 2.5l3 3.2-1.8 2.4c1.2 2.8 3.4 5.1 6.2 6.3l2.4-1.8 3.1 3-1.9 3.4C10 18.5 4.5 13 3.2 4.4z" fill="none" stroke="#ffffff" stroke-width="1.8" stroke-linejoin="round"/>
          </svg>
          <span>(555) 218-4470</span>
        </li>
        <li>
          <svg class="contact-icon" viewBox="0 0 24 24" aria-hidden="true">
            <rect x="3" y="5.5" width="18" height="13" fill="none" stroke="#ffffff" stroke-width="1.8"/>
            <path d="M3 6l9 7 9-7" fill="none" stroke="#ffffff" stroke-width="1.8"/>
          </svg>
          <span>info@corvathproperties.com</span>
        </li>
      </ul>

      <address class="address">1187 Larkspur Bend<br>Salem, OR 97304</address>

      <p class="website">www.corvathproperties.com</p>
    </section>
  </article>
</body>
</html>
```